Illustration / Infographic for HOMEVANTĀ®

I'm a Canadian real estate agent who offers a 50% cashback program to Buyers on my commission.

I also offer two packages to Sellers;
-2.5% full service model
-$999 Flat Fee PVR

I need to be able to explain my CashBack incentive program, 2.5% Full Service, & $999 Flat Fee PVR in an easy to understand and read format.

I have attached my current graphic, which many people still don't understand. I need it more visually appealing / web 2.0 style.

I would like a illustration / infographic that can be use for both the 50% CashBack, 2.5%, and $999 Flat Fee.

You can learn more about my program here:
http://kelbor-trune.ca/sell-your-home-for-less-victoria/
http://kelbor-trune.ca/999-flat-fee-pvr/
http://kelbor-trune.ca/cash-back-program/

Don't worry on the content details, just layout and design for now, and then I will provide winner with required details. I have attached my attempt to create an illustration in photoshop. Would prefer .PSD

Target Market(s)

New Home Buyers
General Public with little to no knowledge of Homevant commissions

Industry/Entity Type

Real Estate

Font styles to use
Sans Serif

Colors
3276b5
33a6d7
faee3e
1b1b1b
eb1f27

Requirements
Must have
• Photoshop

```html
<!DOCTYPE html>
<html lang="en">
<head>
<meta charset="utf-8">
<title>Homevant – Buyer CashBack Incentive Program and Seller Packages</title>
<link rel="stylesheet" href="https://fonts.googleapis.com/css2?family=Source+Sans+3:wght@600;700;800&display=swap">
<style>
  :root {
    --brand-dark: #2b6e9b;
    --brand-blue: #33a6d7;
    --panel-blue: #d3ebf7;
    --text-grey: #808080;
    --white: #ffffff;
    --house-tone: #e9e9e9;
    --house-roof: #e2453f;
    --people-tone: #4a4a4a;
    --pig-tone: #f7b3ae;
  }
  * { box-sizing: border-box; margin: 0; padding: 0; }
  html, body { width: 1200px; height: 777px; overflow: hidden; background: var(--white); }
  body { font-family: "Source Sans 3", Arial, sans-serif; }
  .canvas { position: relative; width: 1200px; height: 777px; background: var(--white); overflow: hidden; }

  .audience-tab {
    position: absolute; left: 0; top: 0; width: 382px; height: 82px;
    background: var(--brand-dark); color: var(--white);
    font-size: 52px; font-weight: 700; line-height: 1; padding: 12px 0 0 86px; letter-spacing: 0.5px;
  }

  .seller-packages { position: absolute; left: 24px; top: 98px; width: 340px; }
  .seller-packages-label { color: var(--text-grey); font-size: 17px; font-weight: 700; line-height: 20px; }
  .seller-package-list { display: flex; gap: 10px; margin-top: 8px; list-style: none; }
  .seller-package {
    background: var(--brand-dark); color: var(--white);
    font-size: 17px; font-weight: 700; line-height: 32px; padding: 0 12px; border-radius: 16px;
  }
  .seller-package-flat { background: var(--brand-blue); }

  .headline-panel {
    position: absolute; left: 382px; top: 0; width: 818px; height: 213px;
    background: var(--panel-blue); color: var(--brand-blue);
  }
  .headline-upto { position: absolute; left: 89px; top: 8px; font-size: 29px; font-weight: 700; line-height: 1.2; }
  .headline-figure {
    position: absolute; left: 86px; top: 49px; font-size: 150px; font-weight: 800; line-height: 1;
    letter-spacing: -4px; transform: scaleX(1.32); transform-origin: left top;
  }
  .headline-percent { position: absolute; left: 300px; top: 73px; font-size: 90px; font-weight: 800; line-height: 1; }
  .headline-title { position: absolute; left: 368px; top: 45px; font-size: 96px; font-weight: 700; line-height: 1; letter-spacing: -0.5px; }
  .headline-subtitle { position: absolute; left: 368px; top: 133px; font-size: 51px; font-weight: 700; line-height: 1; }

  .flow-arrows { position: absolute; left: 0; top: 0; }

  .price-label {
    position: absolute; left: 164px; top: 180px; width: 160px;
    text-align: center; color: var(--brand-blue); font-size: 24px; font-weight: 700; line-height: 1.12;
  }
  .price-tag {
    position: absolute; left: 175px; top: 242px; width: 139px; height: 42px;
    background: var(--brand-blue); color: var(--white); text-align: center;
    font-size: 31px; font-weight: 700; line-height: 42px;
  }
  .price-stem { position: absolute; left: 242px; top: 284px; width: 4px; height: 28px; background: var(--brand-blue); }

  .illustration { position: absolute; border-radius: 6px; }
  .illustration-house { left: 94px; top: 290px; width: 240px; height: 250px; background: linear-gradient(180deg, var(--house-roof) 0 34%, var(--house-tone) 34% 100%); }
  .illustration-agents { left: 505px; top: 274px; width: 220px; height: 268px; background: linear-gradient(180deg, #6e6e6e, var(--people-tone)); border-radius: 40px 40px 8px 8px; }
  .illustration-savings { left: 925px; top: 306px; width: 210px; height: 240px; background: radial-gradient(ellipse at 50% 60%, var(--pig-tone) 0 55%, #f3c9c5 75%, var(--white) 100%); }

  .step { position: absolute; top: 590px; text-align: center; font-weight: 700; }
  .step-line { color: var(--brand-blue); font-size: 28px; line-height: 34px; }
  .step-line-muted { color: var(--text-grey); }
  .step-seller { left: 14px; width: 400px; }
  .step-listing { left: 414px; width: 400px; }
  .step-cashback { left: 828px; width: 400px; }
  .step-note { margin-top: 16px; color: var(--text-grey); font-size: 19px; font-weight: 600; line-height: 22px; }
  .step-seller .step-note { margin-top: 26px; padding-right: 28px; }
</style>
</head>
<body>
<main class="canvas">
  <div class="audience-tab">For Buyer</div>

  <aside class="seller-packages">
    <p class="seller-packages-label">Also for Sellers:</p>
    <ul class="seller-package-list">
      <li class="seller-package">2.5% Full Service</li>
      <li class="seller-package seller-package-flat">$999 Flat Fee PVR</li>
    </ul>
  </aside>

  <header class="headline-panel">
    <span class="headline-upto">Up to</span>
    <span class="headline-figure">50</span>
    <span class="headline-percent">%</span>
    <h1 class="headline-title">CashBack</h1>
    <span class="headline-subtitle">Incentive Program</span>
  </header>

  <svg class="flow-arrows" width="1200" height="777" viewBox="0 0 1200 777" aria-hidden="true">
    <polygon fill="#33a6d7" points="0,371 458,371 458,347 507,401 458,455 458,431 0,431"/>
    <polygon fill="#33a6d7" points="742,371 861,371 861,347 911,401 861,455 861,431 742,431"/>
  </svg>

  <div class="price-label">You bought<br>a house for</div>
  <div class="price-tag">$700K</div>
  <div class="price-stem"></div>

  <div class="illustration illustration-house" role="img" aria-label="Illustration of a small white house with a red roof"></div>
  <div class="illustration illustration-agents" role="img" aria-label="Illustration of two real estate agents in business suits"></div>
  <div class="illustration illustration-savings" role="img" aria-label="Illustration of a pink piggy bank with a dollar bill"></div>

  <section class="step step-seller">
    <p class="step-line">Seller may pay</p>
    <p class="step-line step-line-muted">6% on 100K + 3% of balance*</p>
    <p class="step-line">to Listing Brokerage</p>
    <p class="step-note">*Commission structure may differ.</p>
  </section>

  <section class="step step-listing">
    <p class="step-line">Listing Brokerage</p>
    <p class="step-line">shares 1/2 with</p>
    <p class="step-line">Fair Homevant</p>
  </section>

  <section class="step step-cashback">
    <p class="step-line">Ivo gives you</p>
    <p class="step-line">(Buyer) up to 50%</p>
    <p class="step-line">cash back*</p>
    <p class="step-note">*Minimum of $6,750 to be<br>made by Ivo Trune.</p>
  </section>
</main>
</body>
</html>
```